We (R. T. Halvering & Associates, Inc.) are an executive Search firm based in Los Angeles that is exclusively focused in the Med Tech and Health Tech arenas.   I need a logo to communicate that we are a high end search firm, but also that we are focused in the medicine and science arenas called health tech and med tech.  Many of our clients have robotics and artificial intelligence type products, so it is very technology forward.  I tend to gravitate towards clean, sharp aesthetic as opposed to something that is really over the top.
Attached are files with my logo in two different layouts.  In addition to the letterhead and envelope, I also will need an electronic letterhead in Microsoft Word.  I tend to
I look forward to seeing the designs and just let me know if you have any questions.
Dale

```html
<!DOCTYPE html>
<html lang="en">
<head>
<meta charset="utf-8">
<title>R. T. Halvering &amp; Associates, Inc. — Stationery</title>
<link href="https://fonts.googleapis.com/css2?family=Lato:wght@400;700&family=Arimo:wght@400&display=swap" rel="stylesheet">
<style>
  :root{
    --stage:#3b3b3d;
    --paper:#ffffff;
    --ink:#2b2b2b;
    --body:#555555;
    --brand-blue:#4a9ad6;
    --dark:#222222;
    --card-dark:#232323;
    --rule:#cfcfcf;
  }
  *{margin:0;padding:0;box-sizing:border-box}
  html,body{width:1200px;height:824px;overflow:hidden;background:var(--stage)}
  .stage{position:relative;width:1200px;height:824px}
  .sheet{position:absolute;background:var(--paper);box-shadow:0 4px 14px rgba(0,0,0,.45);overflow:hidden}

  /* brand name block */
  .brand{position:absolute;display:flex;align-items:center;gap:10px;font-family:"Lato",sans-serif;font-weight:700;color:var(--ink)}
  .brand-dot{border-radius:50%;background:var(--brand-blue);flex:none}
  .brand-name{line-height:1.1}
  .brand-name .line2{display:block;letter-spacing:.18em}
  .brand.on-dark{color:#fff}
  .brand.on-dark .brand-dot{background:#fff}

  .contact{font-family:"Arimo",sans-serif;color:var(--dark)}
  .contact-row{display:flex;align-items:center;gap:4px}
  .contact-row svg{flex:none}

  .footer-band{position:absolute;left:0;right:0;bottom:0}
  .footer-band .blue{position:absolute;left:0;bottom:0;height:6px;background:var(--brand-blue)}
  .footer-band .tab{position:absolute;right:0;bottom:0;background:var(--dark);color:#e8e8e8;font-family:"Arimo",sans-serif;letter-spacing:.08em;display:flex;align-items:center;justify-content:flex-end;clip-path:polygon(6px 0,100% 0,100% 100%,0 100%)}

  /* letterhead */
  .letterhead{left:23px;top:48px;width:571px;height:739px}
  .letterhead .brand{left:196px;top:26px;font-size:17px}
  .letterhead .brand .line2{font-size:8px}
  .letter{position:absolute;left:61px;top:174px;width:450px;font-family:"Lato",sans-serif;font-size:8.6px;line-height:12.3px;color:var(--body)}
  .letter p{margin-bottom:12.3px;text-align:justify}
  .letter .date{margin-bottom:14px}
  .letter .recipient strong{color:var(--ink)}
  .signature{width:118px;height:18px;background:linear-gradient(90deg,#cfcfcf,#e4e4e4);border-radius:3px;margin-top:2px}
  .letterhead .footer-rule{position:absolute;left:42px;right:42px;top:671px;height:1px;background:var(--rule)}
  .letterhead .contact{position:absolute;top:682px;font-size:9.3px;line-height:10.6px}
  .letterhead .contact.left{left:42px}
  .letterhead .contact.right{right:42px;text-align:right}
  .letterhead .footer-band{height:17px}
  .letterhead .footer-band .blue{right:160px}
  .letterhead .footer-band .tab{width:164px;height:17px;font-size:9px;padding-right:42px}

  /* business cards */
  .card-dark{left:671px;top:102px;width:237px;height:133px;background:var(--card-dark)}
  .card-dark .brand{left:46px;top:52px;font-size:13px}
  .card-dark .brand .line2{font-size:6px}
  .card-front{left:671px;top:294px;width:236px;height:134px}
  .card-front .brand{left:24px;top:20px;font-size:10px;gap:6px}
  .card-front .brand .line2{font-size:4.6px}
  .card-front .person{position:absolute;right:19px;top:65px;text-align:right;font-family:"Arimo",sans-serif}
  .card-front .person .name{color:var(--brand-blue);font-size:6.6px}
  .card-front .person .role{color:var(--dark);font-size:4.8px}
  .card-front .card-rule{position:absolute;left:24px;right:19px;top:75px;height:1px;background:#e2e2e2}
  .card-front .contact{position:absolute;left:24px;top:84px;font-size:4.8px;line-height:6.5px}
  .card-front .footer-band{height:8px}
  .card-front .footer-band .blue{height:4px;right:88px}
  .card-front .footer-band .tab{width:92px;height:8px;font-size:4.4px;padding-right:18px}

  /* envelope */
  .envelope{left:622px;top:499px;width:555px;height:261px}
  .envelope .brand{left:33px;top:40px;font-size:18px}
  .envelope .brand .line2{font-size:8.4px}
  .envelope .contact{position:absolute;left:33px;top:172px;font-size:8.6px;line-height:10.6px}
  .envelope .footer-band{height:17px}
  .envelope .footer-band .blue{height:7px;right:122px}
  .envelope .footer-band .tab{width:126px;height:17px;font-size:8.4px;padding-right:22px}
</style>
</head>
<body>
<div class="stage">

  <!-- Letterhead -->
  <section class="sheet letterhead">
    <div class="brand">
      <span class="brand-dot" style="width:14px;height:14px"></span>
      <span class="brand-name">R. T. HALVERING<span class="line2">&amp; ASSOCIATES INC.</span></span>
    </div>

    <div class="letter">
      <p class="date">01 January 2050</p>
      <p class="recipient" style="text-align:left"><strong>Company (Pvt) Ltd.</strong><br>PO Box 3355 Mainville St<br>Sample City Country 3355</p>
      <p style="text-align:left">Dear Alan Whitcombe,</p>
      <p>Dolor sit amet, consectetuer adipiscing elit, sed diam nonummy nibh euismod tincidunt ut laoreet dolore magna aliquam erat volutpat. Ut wisi enim ad minim veniam, quis nostrud exerci tation ullamcorper suscipit lobortis nisl ut aliquip ex ea commodo consequat. Duis dolore te feugait nulla facilisi. Nam liber tempor cum soluta nobis eleifend option congue nihil imperdiet doming id quod mazim placerat facer possim assum. Lorem ipsum dolor sit amet, consectetuer adipiscing elit, sed diam nonummy nibh euismod tincidunt ut laoreet dolore magna aliquam erat volutpat. Ut wisi enim ad minim veniam, quis nostrud exerci tation ullamcorper suscipit lobortis nisl ut aliquip ex ea commodo consequat.</p>
      <p>Consectetuer adipiscing elit, sed diam nonummy nibh euismod tincidunt ut laoreet dolore magna aliquam erat volutpat. Ut wisi enim ad minim veniam, quis nostrud exerci tation ullamcorper suscipit lobortis nisl ut aliquip ex ea commodo consequat. Consectetuer adipiscing elit, sed diam nonummy nibh euismod tincidunt ut laoreet dolore magna aliquam erat volutpat. Ut wisi enim ad minim veniam, quis nostrud exerci tation ullamcorper suscipit lobortis nisl ut aliquip ex ea commodo consequat.</p>
      <p>Sed diam nonummy nibh euismod tincidunt ut laoreet dolore magna aliquam erat volutpat. Ut wisi enim ad minim veniam, quis nostrud exerci tation ullamcorper suscipit lobortis nisl ut aliquip ex ea commodo consequat. Consectetuer adipiscing elit, sed diam nonummy nibh euismod tincidunt ut laoreet dolore magna aliquam erat volutpat. Ut wisi enim ad minim veniam, quis nostrud exerci tation ullamcorper suscipit lobortis nisl ut aliquip ex ea commodo consequat.</p>
      <p style="margin:36px 0 0;text-align:left">Sincerely Yours</p>
      <div class="signature" role="img" aria-label="Handwritten signature of Dale Halvering"></div>
    </div>

    <div class="footer-rule"></div>
    <div class="contact left">
      <div class="contact-row"><svg width="8" height="7" viewBox="0 0 8 7"><path d="M1 1h2l.6 1.6-1 .7a4 4 0 0 0 2 2l.7-1L7 5v1.5C4 7 1 4 1 1z" fill="#4a9ad6"/></svg>+1.310.555.0142</div>
      <div class="contact-row"><svg width="8" height="7" viewBox="0 0 8 7"><rect x="2" y="0.5" width="4" height="2" fill="#4a9ad6"/><rect x="0.5" y="2.5" width="7" height="3" fill="#4a9ad6"/><rect x="2" y="5" width="4" height="1.8" fill="#4a9ad6"/></svg>+1.310.555.0147</div>
      <div class="contact-row"><svg width="8" height="7" viewBox="0 0 8 7"><rect x="0.5" y="1" width="7" height="5" fill="#4a9ad6"/><path d="M0.5 1l3.5 3 3.5-3" stroke="#fff" stroke-width=".8" fill="none"/></svg>hello@rthalvering.com</div>
    </div>
    <div class="contact right">2480 Ocean Park Blvd<br>Suite #410<br>Santa Monica CA 90405</div>

    <div class="footer-band">
      <div class="blue"></div>
      <div class="tab">www.rthalvering.com</div>
    </div>
  </section>

  <!-- Business card, back -->
  <section class="sheet card-dark">
    <div class="brand on-dark">
      <span class="brand-dot" style="width:10px;height:10px"></span>
      <span class="brand-name">R. T. HALVERING<span class="line2">&amp; ASSOCIATES INC.</span></span>
    </div>
  </section>

  <!-- Business card, front -->
  <section class="sheet card-front">
    <div class="brand">
      <span class="brand-dot" style="width:8px;height:8px"></span>
      <span class="brand-name">R. T. HALVERING<span class="line2">&amp; ASSOCIATES INC.</span></span>
    </div>
    <div class="person"><div class="name">Dale Halvering</div><div class="role">Executive Recruiter</div></div>
    <div class="card-rule"></div>
    <div class="contact">
      <div class="contact-row"><svg width="5" height="4" viewBox="0 0 8 7"><path d="M1 1h2l.6 1.6-1 .7a4 4 0 0 0 2 2l.7-1L7 5v1.5C4 7 1 4 1 1z" fill="#4a9ad6"/></svg>+1.310.555.0142</div>
      <div class="contact-row"><svg width="5" height="4" viewBox="0 0 8 7"><rect x="0.5" y="1.5" width="7" height="4" fill="#4a9ad6"/></svg>+1.310.555.0147</div>
      <div class="contact-row"><svg width="5" height="4" viewBox="0 0 8 7"><rect x="0.5" y="1" width="7" height="5" fill="#4a9ad6"/></svg>hello@rthalvering.com</div>
      <div style="margin-top:2px">2480 Ocean Park Blvd<br>Suite #410, Santa Monica CA 90405</div>
    </div>
    <div class="footer-band">
      <div class="blue"></div>
      <div class="tab">www.rthalvering.com</div>
    </div>
  </section>

  <!-- Envelope -->
  <section class="sheet envelope">
    <div class="brand">
      <span class="brand-dot" style="width:15px;height:15px"></span>
      <span class="brand-name">R. T. HALVERING<span class="line2">&amp; ASSOCIATES INC.</span></span>
    </div>
    <div class="contact">
      <div class="contact-row"><svg width="8" height="7" viewBox="0 0 8 7"><path d="M1 1h2l.6 1.6-1 .7a4 4 0 0 0 2 2l.7-1L7 5v1.5C4 7 1 4 1 1z" fill="#4a9ad6"/></svg>+1.310.555.0142</div>
      <div class="contact-row"><svg width="8" height="7" viewBox="0 0 8 7"><rect x="2" y="0.5" width="4" height="2" fill="#4a9ad6"/><rect x="0.5" y="2.5" width="7" height="3" fill="#4a9ad6"/><rect x="2" y="5" width="4" height="1.8" fill="#4a9ad6"/></svg>+1.310.555.0147</div>
      <div class="contact-row"><svg width="8" height="7" viewBox="0 0 8 7"><rect x="0.5" y="1" width="7" height="5" fill="#4a9ad6"/><path d="M0.5 1l3.5 3 3.5-3" stroke="#fff" stroke-width=".8" fill="none"/></svg>hello@rthalvering.com</div>
      <div style="margin-top:5px">2480 Ocean Park Blvd<br>Suite #410, Santa Monica CA 90405</div>
    </div>
    <div class="footer-band">
      <div class="blue"></div>
      <div class="tab">www.rthalvering.com</div>
    </div>
  </section>

</div>
</body>
</html>
```